Magazine Ad for TuneHaven School of Music

This will be an ad for music lessons. Logo and text are included in sections below. It will be used for print in newspapers and magazines, so it must look good in black & white as well as in color.

We need an 8.5" x 11" magazine ad (full page), also a 8.5" x 5.5" ad (half page), a 4.25" x 5.5" ad (quarter page) and a business card size ad.

Target Market(s)

Active mothers with children

Industry/Entity Type

School

Font styles to use
Serif

Requirements
Must have
• Must use one of the company logos (see uploaded files).
• All these ads should include the following text:
• ______________
• Music lessons in the comfort of YOUR HOUSE with EXPERIENCED and professional staff.
• Piano, Guitar, voice, VIOLIN, Drums, songwriting, and others
• Email contact@tunehavenlessons.org or call 508-647-3052
• www.TuneHavenLessons.org
• ______________
• The ad must look stylish and sharp in both color and black & white.

```html
<!DOCTYPE html>
<html lang="en">
<head>
<meta charset="utf-8">
<title>TuneHaven School of Music – Magazine Ad</title>
<link rel="stylesheet" href="https://fonts.googleapis.com/css2?family=Roboto+Slab:wght@300;400;500;700;800&display=swap">
<style>
  :root {
    --purple: #8a2590;
    --ink: #1d1d1d;
    --white: #ffffff;
    --icon-cream: #f6f0de;
    --icon-dark: #111111;
    --photo-sky: #c9d1c2;
    --photo-mid: #9fa58f;
    --photo-warm: #b7a88a;
    --photo-ground: #d8d2bd;
  }
  * { margin: 0; padding: 0; box-sizing: border-box; }
  html, body { width: 927px; height: 1200px; overflow: hidden; background: var(--white); }
  .ad {
    position: relative;
    width: 927px;
    height: 1200px;
    overflow: hidden;
    font-family: "Roboto Slab", Georgia, serif;
  }
  .ad-photo {
    position: absolute;
    inset: 0;
    background:
      radial-gradient(ellipse 420px 520px at 160px 520px, rgba(150, 120, 90, 0.55), transparent 70%),
      radial-gradient(ellipse 300px 380px at 860px 1100px, rgba(40, 40, 40, 0.35), transparent 70%),
      linear-gradient(180deg, var(--photo-sky) 0%, var(--photo-mid) 45%, var(--photo-warm) 75%, var(--photo-ground) 100%);
  }
  .brand-box {
    position: absolute;
    left: 334px;
    top: 68px;
    width: 593px;
    height: 189px;
    background: var(--white);
  }
  .brand-mark {
    position: absolute;
    left: 362px;
    top: 104px;
  }
  .brand-name {
    position: absolute;
    left: 536px;
    top: 122px;
    color: var(--ink);
    font-weight: 700;
    line-height: 1;
  }
  .brand-name .name-main { display: block; font-size: 54px; }
  .brand-name .name-sub { display: block; font-size: 23px; font-weight: 700; margin-top: 12px; padding-left: 64px; }

  .headline {
    position: absolute;
    left: 336px;
    top: 270px;
    color: var(--white);
    font-weight: 800;
    text-shadow: 1px 1px 3px rgba(0, 0, 0, 0.55);
    line-height: 53px;
  }
  .headline .line { display: block; white-space: nowrap; }
  .headline .small { font-size: 27px; }
  .headline .mid { font-size: 30px; }
  .headline .big { font-size: 50px; }

  .lesson-band {
    position: absolute;
    left: 0;
    top: 718px;
    width: 927px;
    height: 152px;
  }
  .lesson-label {
    font-family: "Roboto Slab", Georgia, serif;
    font-weight: 400;
    font-size: 19px;
    fill: var(--white);
    text-anchor: middle;
  }

  .contact-box {
    position: absolute;
    left: 0;
    top: 1098px;
    width: 742px;
    height: 102px;
    background: var(--white);
    padding: 19px 0 0 23px;
    color: var(--ink);
    font-weight: 300;
    font-size: 26px;
    line-height: 39px;
    white-space: nowrap;
  }
</style>
</head>
<body>
<main class="ad">
  <div class="ad-photo" role="img" aria-label="Photo of a barefoot young boy sitting on a step playing a wooden flute while a black and white cat looks up at him"></div>

  <section class="brand-box" aria-label="TuneHaven School of Music"></section>
  <svg class="brand-mark" width="150" height="118" viewBox="0 0 150 118" aria-hidden="true">
    <circle cx="75" cy="59" r="57" fill="var(--purple)"/>
  </svg>
  <h1 class="brand-name">
    <span class="name-main">TuneHaven</span>
    <span class="name-sub">School of Music</span>
  </h1>

  <p class="headline">
    <span class="line"><span class="mid">Music lessons</span> <span class="small">in the comfort of</span></span>
    <span class="line"><span class="big">YOUR HOUSE</span> <span class="small">with</span></span>
    <span class="line"><span class="big">EXPERIENCED</span> <span class="small">and</span></span>
    <span class="line"><span class="big">professional</span> <span class="small">staff.</span></span>
  </p>

  <svg class="lesson-band" width="927" height="152" viewBox="0 0 927 152" aria-label="Lessons offered: piano, guitar, voice, violin, drums, songwriting and others">
    <defs>
      <filter id="tile-shadow" x="-10%" y="-10%" width="130%" height="130%">
        <feDropShadow dx="5" dy="5" stdDeviation="3" flood-color="#280a2d" flood-opacity="0.45"/>
      </filter>
    </defs>
    <g filter="url(#tile-shadow)" fill="var(--purple)">
      <polygon points="0,0 127,0 87,144 0,144"/>
      <polygon points="133,0 260,0 220,144 93,144"/>
      <polygon points="266,0 393,0 353,144 226,144"/>
      <polygon points="399,0 526,0 486,144 359,144"/>
      <polygon points="532,0 659,0 619,144 492,144"/>
      <polygon points="665,0 792,0 752,144 625,144"/>
      <polygon points="798,0 927,0 927,144 758,144"/>
    </g>

    <!-- piano -->
    <g class="icon-piano" transform="translate(50 52)">
      <rect x="-30" y="-28" width="60" height="54" fill="var(--icon-cream)"/>
      <g stroke="var(--icon-dark)" stroke-width="2">
        <line x1="-15" y1="-28" x2="-15" y2="26"/><line x1="0" y1="-28" x2="0" y2="26"/><line x1="15" y1="-28" x2="15" y2="26"/>
      </g>
      <g fill="var(--icon-dark)">
        <rect x="-21" y="-28" width="10" height="32"/><rect x="-6" y="-28" width="10" height="32"/>
        <rect x="9" y="-28" width="10" height="32"/><rect x="22" y="-28" width="8" height="32"/>
      </g>
    </g>
    <!-- guitar -->
    <g class="icon-guitar" transform="translate(183 52) rotate(-35)">
      <rect x="-3" y="-40" width="6" height="42" fill="var(--icon-dark)"/>
      <rect x="-6" y="-46" width="12" height="9" rx="2" fill="var(--icon-dark)"/>
      <circle cx="0" cy="10" r="13" fill="var(--icon-cream)"/>
      <circle cx="0" cy="28" r="17" fill="var(--icon-cream)"/>
      <circle cx="0" cy="14" r="5" fill="var(--icon-dark)"/>
      <rect x="-7" y="28" width="14" height="4" fill="var(--icon-dark)"/>
    </g>
    <!-- microphone -->
    <g class="icon-mic" transform="translate(316 50)">
      <circle cx="10" cy="-20" r="13" fill="var(--icon-cream)"/>
      <path d="M2 -12 L-22 8 L-16 14 L8 -6 Z" fill="var(--icon-dark)"/>
      <rect x="-4" y="10" width="6" height="24" fill="var(--icon-dark)"/>
      <ellipse cx="-1" cy="36" rx="14" ry="4" fill="var(--icon-dark)"/>
    </g>
    <!-- violin -->
    <g class="icon-violin" transform="translate(449 52) rotate(40)">
      <ellipse cx="0" cy="-6" rx="12" ry="13" fill="var(--icon-cream)"/>
      <ellipse cx="0" cy="16" rx="16" ry="17" fill="var(--icon-cream)"/>
      <rect x="-2.5" y="-44" width="5" height="42" fill="var(--icon-dark)"/>
      <circle cx="0" cy="-46" r="4" fill="var(--icon-dark)"/>
      <rect x="-7" y="10" width="14" height="3" fill="var(--icon-dark)"/>
      <g stroke="var(--icon-dark)" stroke-width="1"><line x1="-1.5" y1="-4" x2="-1.5" y2="28"/><line x1="1.5" y1="-4" x2="1.5" y2="28"/></g>
    </g>
    <!-- drums -->
    <g class="icon-drums" transform="translate(582 52)">
      <g stroke="var(--icon-cream)" stroke-width="2">
        <line x1="-28" y1="-24" x2="-22" y2="34"/><line x1="28" y1="-24" x2="22" y2="34"/>
        <line x1="-36" y1="34" x2="36" y2="34"/>
      </g>
      <ellipse cx="-28" cy="-26" rx="12" ry="3" fill="var(--icon-cream)"/>
      <ellipse cx="28" cy="-26" rx="12" ry="3" fill="var(--icon-cream)"/>
      <rect x="-24" y="-4" width="16" height="12" fill="var(--icon-cream)"/>
      <rect x="8" y="-12" width="16" height="14" fill="var(--icon-cream)"/>
      <circle cx="0" cy="16" r="16" fill="var(--icon-cream)"/>
      <circle cx="0" cy="16" r="6" fill="var(--icon-dark)"/>
    </g>
    <!-- songwriting -->
    <g class="icon-songwriting" transform="translate(715 52)">
      <rect x="-26" y="-30" width="40" height="56" rx="3" fill="var(--icon-cream)"/>
      <g stroke="var(--icon-dark)" stroke-width="2">
        <line x1="-20" y1="-18" x2="8" y2="-18"/><line x1="-20" y1="-8" x2="8" y2="-8"/><line x1="-20" y1="2" x2="0" y2="2"/>
      </g>
      <ellipse cx="-12" cy="16" rx="6" ry="4.5" fill="var(--icon-dark)"/>
      <rect x="-7.5" y="-2" width="2.5" height="18" fill="var(--icon-dark)"/>
      <path d="M24 -26 L30 -20 L4 14 L-2 16 L0 8 Z" fill="var(--icon-dark)"/>
    </g>
    <!-- saxophone -->
    <g class="icon-sax" transform="translate(850 52)">
      <path d="M-14 -38 L-8 -38 L-2 -26 L-2 16 Q-2 28 10 28 Q20 28 20 16 L20 6 L28 2 L30 8 L26 10 L26 18 Q26 36 10 36 Q-10 36 -10 16 L-10 -26 Z" fill="var(--icon-dark)"/>
      <path d="M-14 -38 L-26 -42 L-26 -36 L-14 -34 Z" fill="var(--icon-cream)"/>
      <g fill="var(--icon-cream)"><circle cx="-6" cy="-12" r="2"/><circle cx="-6" cy="-2" r="2"/><circle cx="-6" cy="8" r="2"/></g>
    </g>

    <text class="lesson-label" x="44" y="130">PIANO</text>
    <text class="lesson-label" x="161" y="130">GUITAR</text>
    <text class="lesson-label" x="294" y="130">VOICE</text>
    <text class="lesson-label" x="427" y="130">VIOLIN</text>
    <text class="lesson-label" x="560" y="130">DRUMS</text>
    <text class="lesson-label" x="693" y="130" textLength="112" lengthAdjust="spacingAndGlyphs">SONGWRITING</text>
    <text class="lesson-label" x="838" y="130">OTHERS</text>
  </svg>

  <footer class="contact-box">
    Email: contact@tunehavenlessons.org or<br>
    call 508-647-3052. www.TuneHavenLessons.org
  </footer>
</main>
</body>
</html>
```